Enhance the web site presence of Kolrith Global Limited

Upgrade the current web site www.kolrithpanel.com to share with the audience our current plan and future developments of our company. I have created a worksheet which shows all the pages that I like to have. The home page in English, Japanese and Chinese is hyperlinked to the various pages. Under the product, we should allow the user to select "single sided PCB or double sided PCB". The translation of the contents of the pages with Japanese is not complete but the English and Chinese are complete. You can download the briefing and photos in the dropbox files below;

https://www.sharelocker.net/sh/xk4trw92mpd3ab1/BBQm_Lp841zzPq2Rw7KtYnHjEa?dl=0

Target Market(s)

Electronic companies

Industry/Entity Type

Electronic

Coding

Coded - Design and coding required

Number of Pages Required

5+ page

Font styles to use
Sans Serif

Colors
00a990
0353a1
33b8a4

Requirements
Must have
• Get a sense of confidence on our company's integrity and capability to deliver the highest quality PCBs with the most competitive prices and best services. A sense of elegance is essential as we DON'T treat profits as the number one goal. Our number goal is to do the RIGHT things right. Having a mixture of our company photos will be appropriate.

```html
<!DOCTYPE html>
<html lang="en">
<head>
<meta charset="utf-8">
<title>Kolrith Global Limited — Printed Circuit Boards</title>
<link rel="stylesheet" href="https://fonts.googleapis.com/css2?family=Source+Sans+3:wght@400;600;700&family=Open+Sans:wght@400;600&display=swap">
<style>
  :root {
    --teal: #00a990;
    --teal-light: #33b8a4;
    --blue: #0353a1;
    --band-blue: #0a3f9c;
    --band-green: #11654d;
    --ink: #222222;
    --text: #555555;
    --muted: #8a8a8a;
    --card: #eeeeee;
    --clients: #efefef;
    --line: #bdbdbd;
    --footer: #2b2b2b;
    --footer-text: #b8b8b8;
    --white: #ffffff;
  }
  * { box-sizing: border-box; margin: 0; padding: 0; }
  html, body { width: 1200px; height: 2293px; overflow: hidden; }
  body { background: var(--white); font-family: "Open Sans", sans-serif; color: var(--text); position: relative; }

  /* Header */
  .site-header { height: 97px; position: relative; }
  .brand { position: absolute; left: 133px; top: 24px; }
  .brand-name { font-family: "Source Sans 3", sans-serif; font-weight: 700; font-size: 38px; line-height: 38px; color: var(--ink); display: flex; align-items: center; gap: 8px; letter-spacing: 2px; }
  .brand-name i { display: inline-block; width: 14px; height: 14px; background: var(--teal); }
  .brand-tag { font-family: "Source Sans 3", sans-serif; font-size: 8.5px; font-weight: 600; color: var(--ink); margin-top: 2px; letter-spacing: .2px; }
  .login { position: absolute; right: 134px; top: 25px; font-family: "Source Sans 3", sans-serif; font-size: 13px; color: var(--teal); display: flex; align-items: center; gap: 7px; letter-spacing: .3px; }
  .main-nav { position: absolute; right: 134px; top: 57px; display: flex; gap: 32px; }
  .main-nav a { font-family: "Source Sans 3", sans-serif; font-size: 13.5px; color: var(--ink); text-decoration: none; letter-spacing: .3px; }
  .main-nav a.current { color: var(--blue); text-decoration: underline; text-underline-offset: 3px; }

  /* Hero */
  .hero { height: 518px; position: relative; background: linear-gradient(160deg, #b9bcb8 0%, #8c938e 35%, #2f8a4c 60%, #5d6660 100%); }
  .hero-arrow { position: absolute; top: 239px; width: 40px; height: 40px; }
  .hero-arrow.prev { left: 38px; }
  .hero-arrow.next { right: 38px; }

  /* Welcome band */
  .welcome { height: 296px; background: linear-gradient(90deg, var(--band-blue) 0%, #0d4f7c 55%, var(--band-green) 100%); color: var(--white); text-align: center; padding-top: 64px; }
  .welcome h1 { font-family: "Source Sans 3", sans-serif; font-weight: 600; font-size: 33px; letter-spacing: .5px; margin-bottom: 12px; }
  .welcome p { font-size: 11.9px; line-height: 18px; width: 934px; margin: 0 auto 8px; }

  /* Feature cards */
  .features { display: flex; gap: 21px; width: 934px; margin: 79px auto 0; }
  .card { width: 297px; height: 393px; background: var(--card); }
  .card-photo { height: 200px; }
  .card-photo.products { background: linear-gradient(135deg, #d9dcd6, #7f8c84 55%, #1f8f44); }
  .card-photo.capabilities { background: linear-gradient(135deg, #8a9089, #cfd3cf 45%, #2e7a3f); }
  .card-photo.about { background: linear-gradient(180deg, #3f82d6 0%, #9cc3ea 35%, #e9ecea 60%, #2a7b43 100%); }
  .card-body { padding: 20px 12px 0; }
  .card h2 { font-family: "Source Sans 3", sans-serif; font-weight: 600; font-size: 21px; color: var(--teal); margin-bottom: 8px; letter-spacing: .2px; }
  .card p { font-size: 10.8px; line-height: 17px; color: #4a4a4a; }
  .btn-more { display: inline-block; margin-top: 16px; width: 89px; height: 35px; border: 1px solid var(--line); font-size: 11px; color: var(--muted); text-align: center; line-height: 33px; }

  /* Clients */
  .clients { position: absolute; top: 1463px; left: 0; width: 1200px; height: 240px; background: var(--clients); text-align: center; }
  .clients h3 { font-family: "Source Sans 3", sans-serif; font-weight: 600; font-size: 21px; color: var(--teal); margin-top: 64px; letter-spacing: .5px; }
  .client-list { width: 934px; margin: 38px auto 0; display: flex; justify-content: space-between; align-items: center; }
  .client { font-family: "Source Sans 3", sans-serif; font-weight: 600; font-size: 19px; color: #6e6e6e; display: flex; align-items: center; gap: 8px; }
  .client i { width: 14px; height: 14px; background: #9a9a9a; display: inline-block; }
  .client i.round { border-radius: 50%; }

  /* Contact */
  .contact { position: absolute; top: 1776px; left: 0; width: 1200px; text-align: center; }
  .contact h2 { font-family: "Source Sans 3", sans-serif; font-weight: 600; font-size: 35px; color: var(--teal); letter-spacing: .5px; }
  .contact-intro { width: 934px; margin: 12px auto 0; font-size: 14px; line-height: 23px; color: #666; }
  .contact-form { width: 934px; margin: 24px auto 0; }
  .field-row { display: flex; gap: 21px; }
  .field { flex: 1; height: 41px; border: 1px solid var(--line); text-align: left; padding-left: 14px; font-size: 12px; line-height: 39px; color: #555; }
  .field.message { margin-top: 23px; }
  .btn-submit { display: block; margin: 25px auto 0; width: 89px; height: 39px; background: var(--ink); color: var(--white); font-family: "Source Sans 3", sans-serif; font-size: 13px; letter-spacing: .3px; line-height: 39px; }

  /* Footer */
  .site-footer { position: absolute; top: 2149px; left: 0; width: 1200px; height: 144px; background: var(--footer); text-align: center; color: var(--footer-text); }
  .footer-nav { margin-top: 28px; font-size: 11px; }
  .footer-nav span { margin: 0 7px; }
  .copyright { margin-top: 13px; font-size: 10.5px; }
  .social { margin-top: 26px; display: flex; justify-content: center; gap: 20px; font-size: 11px; }
</style>
</head>
<body>

<header class="site-header">
  <div class="brand">
    <div class="brand-name"><i></i>KGL</div>
    <div class="brand-tag">Quality Circuit Boards Built With Care</div>
  </div>
  <div class="login">
    <svg width="12" height="12" viewBox="0 0 12 12" aria-hidden="true"><path d="M1 6h6M4.5 3.5L7 6 4.5 8.5" stroke="currentColor" stroke-width="1.6" fill="none"/><path d="M7.5 1H11v10H7.5" stroke="currentColor" stroke-width="1.4" fill="none"/></svg>
    CUSTOMER LOG IN
  </div>
  <nav class="main-nav">
    <a class="current" href="#">HOME</a>
    <a href="#">PRODUCTS</a>
    <a href="#">FACILITIES</a>
    <a href="#">CUSTOMERS</a>
    <a href="#">NEWS</a>
    <a href="#">QUOTES</a>
    <a href="#">CONTACT US</a>
  </nav>
</header>

<section class="hero" role="img" aria-label="Factory floor with stacks of green printed circuit boards beside a processing machine">
  <svg class="hero-arrow prev" viewBox="0 0 40 40" aria-hidden="true"><circle cx="20" cy="20" r="18" fill="#1c3a8a" stroke="#fff" stroke-width="3"/><path d="M23 12l-8 8 8 8" stroke="#fff" stroke-width="4" fill="none"/></svg>
  <svg class="hero-arrow next" viewBox="0 0 40 40" aria-hidden="true"><circle cx="20" cy="20" r="18" fill="#1a2a4a" stroke="#fff" stroke-width="3"/><path d="M17 12l8 8-8 8" stroke="#fff" stroke-width="4" fill="none"/></svg>
</section>

<section class="welcome">
  <h1>WELCOME TO KOLRITH GLOBAL LIMITED (KGL)</h1>
  <p>Established in 2007, Kolrith Global Limited (KGL) is a Hong Kong company specializing in single and double sized printed circuit boards. Its manufacturing facility is located in a self-owned facility in Tangxia, Dongguan of China which is 50 minutes from Hong Kong.</p>
  <p>Our mission is to become a premium low costs PCB supplier that fully embraces human, social and environmental responsibilities.</p>
  <p>Through our insatiable drive to maximize efficiency, KGL is becoming a highly efficient PCB factory with a capacity of 140,000 square meter a month.</p>
  <p>PCB is our business and it is through continued automation and innovation that will drive our growth in the next 10 years.</p>
</section>

<section class="features">
  <article class="card">
    <div class="card-photo products" role="img" aria-label="Production line conveyor carrying circuit boards"></div>
    <div class="card-body">
      <h2>OUR PRODUCTS</h2>
      <p>Maecenas vel tortor accumsan quam varius imperdiet vel eget elit. Aenean facilisis tincidunt lectus, id dictum nisi luctus eget. Vivamus efficitur ex condimentum, malesuada eros eget.</p>
      <span class="btn-more">Read more</span>
    </div>
  </article>
  <article class="card">
    <div class="card-photo capabilities" role="img" aria-label="Automated printing machine working on a green circuit board"></div>
    <div class="card-body">
      <h2>TECHNICAL CAPABILITIES</h2>
      <p>Maecenas vel tortor accumsan quam varius imperdiet vel eget elit. Aenean facilisis tincidunt lectus, id dictum nisi luctus eget. Vivamus efficitur ex condimentum, malesuada eros eget.</p>
      <span class="btn-more">Read more</span>
    </div>
  </article>
  <article class="card">
    <div class="card-photo about" role="img" aria-label="Company factory building under a blue sky"></div>
    <div class="card-body">
      <h2>ABOUT US</h2>
      <p>Maecenas vel tortor accumsan quam varius imperdiet vel eget elit. Aenean facilisis tincidunt lectus, id dictum nisi luctus eget. Vivamus efficitur ex condimentum, malesuada eros eget.</p>
      <span class="btn-more">Read more</span>
    </div>
  </article>
</section>

<section class="clients">
  <h3>CLIENTS</h3>
  <div class="client-list">
    <span class="client">Northvale Circuits</span>
    <span class="client">Hallmer Werkstoff<i class="round"></i></span>
    <span class="client">Ornika</span>
    <span class="client">Taberu/Vane</span>
    <span class="client"><i></i>Moldaxis</span>
  </div>
</section>

<section class="contact">
  <h2>CONTACT US</h2>
  <p class="contact-intro">Maecenas vel tortor accumsan quam varius imperdiet vel eget elit. Aenean facilisis tincidunt lectus, id dictum nisi luctus eget. Vivamus efficitur ex condimentum, malesuada eros eget</p>
  <div class="contact-form">
    <div class="field-row">
      <div class="field">Name</div>
      <div class="field">Company name</div>
      <div class="field">Email Address</div>
      <div class="field">Subject</div>
    </div>
    <div class="field message">Messages</div>
    <span class="btn-submit">SUBMIT</span>
  </div>
</section>

<footer class="site-footer">
  <div class="footer-nav">Home<span>|</span>Products<span>|</span>Facilities<span>|</span>Customers<span>|</span>News<span>|</span>Quotes<span>|</span>Contact Us</div>
  <div class="copyright">Copyright © 2018 Kolrith Global Limited (KGL). All rights reserved.</div>
  <div class="social"><span>Linkora</span><span>Chirpline</span><span>Vidstream</span><span>Snapfeed</span></div>
</footer>

</body>
</html>
```